Financial PR company Homepage and Inner Page design

Please design a web homepage and innerpage for OVIN Public Relations.
OVIN Public Relations is a Financial PR company targeting Shenzhen Qian Special Economical Zone.
Note:
1. Menu includes ( Please specialize in Chinese and we want to see the Chinese fonts)
关于我们/服务板块/专业优势/合作伙伴/前海商圈/公司新闻/加盟我们/联系我们

2. Please refer to world class PR Business company and contribute your idea on website design and color themes.

3. We have attached the Logo for reference.

4. Anytime use picture for reference, please select asian business people pictures.

Cheers,

HI Designers, Thanks for the design submission. Here is our client feedback: 1. Adopt one screen design. 2. Use amiable Asia Business woman pictures. 3. Use contrastive color theme for the design. Cheers, Kip From TW

```html
<!DOCTYPE html>
<html lang="zh-CN">
<head>
<meta charset="utf-8">
<title>OVIN Public Relations</title>
<link href="https://fonts.googleapis.com/css2?family=Noto+Sans+SC:wght@400;500;700&family=Open+Sans:ital,wght@0,400;0,600;0,700;1,400;1,600&family=Raleway:wght@300;400;600&display=swap" rel="stylesheet">
<style>
:root{
  --navy:#1e3956;
  --navy-dark:#16293f;
  --blue:#2f9ae0;
  --blue-light:#6cc0ef;
  --red:#d9453b;
  --ink:#3a3f46;
  --muted:#8a9099;
  --line:#e3e6ea;
  --grey-bg:#f1f2f4;
  --band:#2a2f37;
  --footer:#1d2836;
  --footer-bottom:#151d28;
  --white:#ffffff;
}
*{box-sizing:border-box;margin:0;padding:0}
html,body{width:1200px;height:2980px;overflow:hidden}
body{font-family:"Open Sans","Noto Sans SC",Arial,sans-serif;color:var(--ink);background:var(--white);font-size:13px}
.zh{font-family:"Noto Sans SC","Open Sans",sans-serif}
.wrap{width:1040px;margin:0 auto;position:relative;height:100%}

/* header */
.site-header{height:120px}
.topline{position:absolute;top:8px;left:0;font-size:11px;color:var(--muted);display:flex;gap:24px}
.brand{position:absolute;left:60px;top:36px;display:flex;align-items:center;gap:14px}
.brand-dot{width:44px;height:44px;border-radius:50%;background:var(--blue)}
.brand-name{font-size:34px;font-weight:700;color:var(--navy);letter-spacing:1px}
.brand-tag{position:absolute;left:118px;top:82px;font-size:12px;color:var(--muted);letter-spacing:3px}
.util-links{position:absolute;right:0;top:8px;display:flex;gap:6px}
.util-links a{font-size:12px;color:var(--muted);text-decoration:none;padding:1px 8px;border-left:1px solid var(--line)}
.util-links a.hot{background:var(--red);color:var(--white);border:0;border-radius:2px}

/* nav */
.main-nav{height:48px;background:var(--navy)}
.main-nav ul{list-style:none;display:flex;height:48px;align-items:stretch}
.main-nav li a{display:flex;align-items:center;height:48px;padding:0 17px;color:var(--white);text-decoration:none;font-size:15px;font-weight:500}
.main-nav li.active a{background:var(--blue)}
.search{position:absolute;right:0;top:11px;width:130px;height:26px;background:var(--blue);border-radius:2px}

/* hero */
.hero{height:412px;position:relative;overflow:hidden;background:linear-gradient(180deg,#8fb8d6 0%,#5e8fb5 45%,#3b6388 100%)}
.hero-person{position:absolute;left:700px;top:22px;width:290px;height:390px;background:linear-gradient(180deg,#c9d9ea 0%,#4f86c2 60%,#2a5b93 100%);border-radius:140px 140px 0 0}
.hero-copy{position:absolute;left:175px;top:105px}
.hero-copy .slab{display:inline-block;background:rgba(20,35,55,.72);color:var(--white);font-style:italic;font-weight:600;font-size:40px;line-height:56px;padding:0 18px;margin-bottom:8px}
.hero-copy .btn{display:inline-block;margin-top:6px;background:var(--blue);color:var(--white);font-size:13px;padding:8px 18px;border-radius:2px}
.hero .arrow{position:absolute;top:180px;width:30px;height:50px}
.hero .arrow.left{left:30px}.hero .arrow.right{right:30px}
.strip{height:72px;background:var(--navy-dark);color:var(--blue-light);text-align:center;font-style:italic;font-size:30px;line-height:72px}

/* section titles */
.section-title{text-align:center}
.section-title .kicker{font-family:"Raleway",sans-serif;font-size:24px;color:var(--ink)}
.section-title h2{font-family:"Raleway",sans-serif;font-weight:400;font-size:36px;letter-spacing:2px;color:var(--navy);margin-top:2px}

/* who */
.who{height:296px;padding-top:28px}
.who-body{display:flex;gap:60px;margin-top:28px;padding:0 60px}
.who-text{flex:1;font-size:13px;line-height:22px;color:var(--muted)}
.who-text b{color:var(--blue);font-weight:600}
.who-stats{flex:1}
.stat{display:flex;height:26px;margin-bottom:10px;background:#dce9f5}
.stat .label{width:140px;background:var(--navy);color:var(--white);font-size:12px;line-height:26px;padding-left:10px}
.stat .fill{background:var(--blue-light)}
.read-more{position:absolute;right:60px;bottom:14px;font-size:12px;color:var(--blue)}

/* services */
.services{height:272px;background:linear-gradient(180deg,#343a44,#23272e);color:var(--white);position:relative}
.services h3{text-align:center;font-family:"Raleway",sans-serif;font-weight:400;font-size:24px;padding-top:22px}
.svc-line{position:absolute;left:120px;right:120px;top:145px;height:2px;background:rgba(255,255,255,.35)}
.svc-row{position:absolute;left:0;right:0;top:110px;display:flex;justify-content:space-around;padding:0 60px}
.svc{width:150px;text-align:center;font-size:14px;line-height:19px;color:var(--blue-light)}
.svc .ring{width:70px;height:70px;border:2px solid var(--white);border-radius:50%;margin:0 auto 10px;display:flex;align-items:center;justify-content:center;background:var(--band)}

/* advantages */
.advantages{height:540px;padding-top:56px}
.adv-grid{display:flex;justify-content:space-between;margin-top:44px;padding:0 90px}
.adv-col{width:300px}
.adv-item{margin-bottom:50px;position:relative}
.adv-col.left .adv-item{text-align:right;padding-right:30px}
.adv-col.right .adv-item{padding-left:30px}
.adv-item h4{font-size:16px;font-weight:600;color:var(--ink)}
.adv-item p{font-size:12px;color:var(--muted);line-height:19px;margin-top:4px}
.adv-item .pip{position:absolute;top:6px;width:10px;height:10px;border-radius:50%;background:var(--blue)}
.adv-col.left .pip{right:0}.adv-col.right .pip{left:0}
.adv-mark{display:flex;align-items:center;gap:12px;margin-top:100px;align-self:flex-start}
.adv-mark .dot{width:56px;height:56px;border-radius:50%;background:var(--blue)}
.adv-mark span{font-size:32px;font-weight:700;color:var(--navy)}

/* process */
.process{height:480px;background:var(--grey-bg);padding-top:44px}
.process .kicker{color:var(--red)}
.cards{display:flex;gap:40px;justify-content:center;margin-top:40px}
.card{width:210px;height:250px;background:var(--white);text-align:center;padding:26px 20px;box-shadow:0 2px 6px rgba(0,0,0,.08)}
.card .icon{width:60px;height:60px;border-radius:50%;background:var(--grey-bg);margin:0 auto 16px;display:flex;align-items:center;justify-content:center}
.card h5{font-size:17px;font-weight:400;color:var(--ink);margin-bottom:10px}
.card p{font-size:12px;line-height:19px;color:var(--muted)}
.card.active{background:var(--blue)}
.card.active h5,.card.active p{color:var(--white)}
.card.active .icon{background:var(--white)}

/* news */
.news{height:428px;padding-top:44px}
.news-box{width:900px;margin:34px auto 0;height:200px;border:1px solid var(--line);background:#fafbfc;position:relative;padding:22px 40px 0 220px;font-size:12px;line-height:19px;color:var(--muted)}
.news-img{position:absolute;left:40px;top:70px;width:130px;height:80px;background:linear-gradient(135deg,#e9ecef,#c7ccd3)}
.news-person{position:absolute;left:320px;top:110px;display:flex;align-items:center;gap:14px}
.news-person .avatar{width:62px;height:62px;border-radius:50%;background:linear-gradient(180deg,#c9b9a8,#6d7684)}
.news-person b{display:block;color:var(--ink);font-size:13px}
.dots{display:flex;gap:8px;justify-content:center;margin-top:18px}
.dots i{width:8px;height:8px;border-radius:50%;background:#c9ced5}
.dots i.on{background:var(--blue)}

/* footer */
.site-footer{height:272px;background:var(--footer);color:#aab3bf}
.foot-grid{display:flex;padding:36px 40px 0;gap:50px}
.foot-col{width:200px;font-size:12px;line-height:22px}
.foot-col h6{font-size:15px;color:var(--white);font-weight:600;margin-bottom:12px}
.foot-brand{font-size:26px;font-weight:700;color:var(--white);display:flex;align-items:center;gap:10px;margin-bottom:12px}
.foot-brand i{width:30px;height:30px;border-radius:50%;background:var(--blue)}
.socials{display:flex;gap:10px;margin-top:12px}
.socials i{width:22px;height:22px;border-radius:50%;background:#3a4758}
.foot-col li{list-style:none}
.foot-col li::before{content:"› ";color:var(--blue)}
.sub-input{height:28px;background:var(--white);margin-top:10px;border-radius:2px}
.sub-btn{width:70px;height:26px;background:var(--blue);color:var(--white);font-size:11px;text-align:center;line-height:26px;margin-top:8px;margin-left:auto;border-radius:2px}
.foot-bottom{height:40px;background:var(--footer-bottom);color:#8893a1;font-size:11px;line-height:40px}
.foot-bottom .links{position:absolute;right:40px;top:0;display:flex;gap:20px}
</style>
</head>
<body>

<header class="site-header">
  <div class="wrap">
    <div class="topline"><span>+86 755 0100 2200</span><span>hello@ovinpr.example</span></div>
    <div class="brand"><span class="brand-dot"></span><span class="brand-name">OVIN PR</span></div>
    <div class="brand-tag zh">OVIN 公共关系有限公司</div>
    <nav class="util-links zh"><a class="hot" href="#">博客</a><a href="#">登录</a><a href="#">联系我们</a></nav>
  </div>
</header>

<nav class="main-nav zh">
  <div class="wrap">
    <ul>
      <li class="active"><a href="#">关于我们</a></li>
      <li><a href="#">服务板块</a></li>
      <li><a href="#">专业优势</a></li>
      <li><a href="#">合作伙伴</a></li>
      <li><a href="#">前海商圈</a></li>
      <li><a href="#">公司新闻</a></li>
      <li><a href="#">加盟我们</a></li>
      <li><a href="#">联系我们</a></li>
    </ul>
    <div class="search"></div>
  </div>
</nav>

<section class="hero" role="img" aria-label="City skyline with a smiling business person">
  <div class="hero-person" role="img" aria-label="Business person in a blue shirt holding a folder"></div>
  <div class="hero-copy">
    <div class="slab">We don't Promise,</div><br>
    <div class="slab">We Act our best</div><br>
    <span class="btn">Learn More</span>
  </div>
  <svg class="arrow left" viewBox="0 0 30 50"><polyline points="22,8 8,25 22,42" fill="none" stroke="#fff" stroke-width="3"/></svg>
  <svg class="arrow right" viewBox="0 0 30 50"><polyline points="8,8 22,25 8,42" fill="none" stroke="#fff" stroke-width="3"/></svg>
</section>
<div class="strip">Offering a wide range of recruitment Solutions</div>

<section class="who">
  <div class="wrap">
    <div class="section-title">
      <div class="kicker">Who We are</div>
      <h2>OVIN PUBLIC RELATIONS COMPANY</h2>
    </div>
    <div class="who-body">
      <p class="who-text"><b>OVIN PR</b> Lorem ipsum dolor sit amet, consectetur adipisicing elit, sed do eiusmod tempor incididunt ut labore et dolore magna aliqua. Ut enim ad minim veniam, quis nostrud exercitation ullamco laboris nisi ut aliquip ex ea commodo consequat.</p>
      <div class="who-stats">
        <div class="stat"><span class="label">Employer</span><span class="fill" style="width:70%"></span></div>
        <div class="stat"><span class="label">Information</span><span class="fill" style="width:50%"></span></div>
        <div class="stat"><span class="label">Candidates</span><span class="fill" style="width:62%"></span></div>
      </div>
    </div>
    <span class="read-more">Read more</span>
  </div>
</section>

<section class="services">
  <h3>Services for Public Relations Company</h3>
  <div class="svc-line"></div>
  <div class="svc-row">
    <div class="svc"><div class="ring"><svg width="30" height="30" viewBox="0 0 30 30"><circle cx="15" cy="10" r="6" fill="none" stroke="#fff" stroke-width="2"/><path d="M4 28c2-8 20-8 22 0" fill="none" stroke="#fff" stroke-width="2"/></svg></div>CEO<br>PR Owner</div>
    <div class="svc"><div class="ring"><svg width="30" height="30" viewBox="0 0 30 30"><rect x="5" y="5" width="20" height="20" fill="none" stroke="#fff" stroke-width="2"/><line x1="9" y1="12" x2="21" y2="12" stroke="#fff" stroke-width="2"/><line x1="9" y1="18" x2="21" y2="18" stroke="#fff" stroke-width="2"/></svg></div>Content Marketing</div>
    <div class="svc"><div class="ring"><svg width="30" height="30" viewBox="0 0 30 30"><polyline points="4,24 12,14 18,19 26,6" fill="none" stroke="#fff" stroke-width="2"/></svg></div>Marketing Services</div>
    <div class="svc"><div class="ring"><svg width="30" height="30" viewBox="0 0 30 30"><path d="M5 12h6l10-6v18l-10-6H5z" fill="none" stroke="#fff" stroke-width="2"/></svg></div>Advocacy Advertising</div>
    <div class="svc"><div class="ring"><svg width="30" height="30" viewBox="0 0 30 30"><circle cx="15" cy="15" r="10" fill="none" stroke="#fff" stroke-width="2"/><line x1="5" y1="15" x2="25" y2="15" stroke="#fff" stroke-width="2"/></svg></div>Public Relations</div>
    <div class="svc"><div class="ring"><svg width="30" height="30" viewBox="0 0 30 30"><circle cx="11" cy="11" r="5" fill="none" stroke="#fff" stroke-width="2"/><circle cx="21" cy="13" r="4" fill="none" stroke="#fff" stroke-width="2"/><path d="M3 26c1-6 15-6 16 0" fill="none" stroke="#fff" stroke-width="2"/></svg></div>Recruitment</div>
  </div>
</section>

<section class="advantages">
  <div class="section-title">
    <div class="kicker">Your Career will boom with OVIN PR</div>
    <h2>ADVANTAGES</h2>
  </div>
  <div class="adv-grid">
    <div class="adv-col left">
      <div class="adv-item"><span class="pip"></span><h4>Marketing</h4><p>Lorem ipsum is simply dummy text of the printing industry.</p></div>
      <div class="adv-item"><span class="pip"></span><h4>Recruitment</h4><p>Lorem ipsum is simply dummy text of the printing industry.</p></div>
      <div class="adv-item"><span class="pip"></span><h4>Services</h4><p>Lorem ipsum is simply dummy text of the printing industry.</p></div>
    </div>
    <div class="adv-mark"><span class="dot"></span><span>OVIN PR</span></div>
    <div class="adv-col right">
      <div class="adv-item"><span class="pip"></span><h4>Public</h4><p>Lorem ipsum is simply dummy text of the printing industry.</p></div>
      <div class="adv-item"><span class="pip"></span><h4>Relations</h4><p>Lorem ipsum is simply dummy text of the printing industry.</p></div>
      <div class="adv-item"><span class="pip"></span><h4>Engagement</h4><p>Lorem ipsum is simply dummy text of the printing industry.</p></div>
    </div>
  </div>
</section>

<section class="process">
  <div class="section-title">
    <div class="kicker">It's not magic! It's powerful and proprietary technology.</div>
    <h2>PROCESS</h2>
  </div>
  <div class="cards">
    <div class="card active"><div class="icon"><svg width="26" height="26" viewBox="0 0 26 26"><rect x="5" y="3" width="16" height="20" fill="none" stroke="#2f9ae0" stroke-width="2"/><line x1="9" y1="9" x2="17" y2="9" stroke="#2f9ae0" stroke-width="2"/><line x1="9" y1="14" x2="17" y2="14" stroke="#2f9ae0" stroke-width="2"/></svg></div><h5>Collect</h5><p>Lorem ipsum is simply dummy text of the printing and typesetting industry. Lorem ipsum has been the standard.</p></div>
    <div class="card"><div class="icon"><svg width="26" height="26" viewBox="0 0 26 26"><circle cx="13" cy="13" r="5" fill="none" stroke="#555" stroke-width="2"/><circle cx="13" cy="13" r="10" fill="none" stroke="#555" stroke-width="2" stroke-dasharray="4 3"/></svg></div><h5>Analyze</h5><p>Lorem ipsum is simply dummy text of the printing and typesetting industry. Lorem ipsum has been the standard.</p></div>
    <div class="card"><div class="icon"><svg width="26" height="26" viewBox="0 0 26 26"><path d="M2 13c5-8 17-8 22 0c-5 8-17 8-22 0z" fill="none" stroke="#555" stroke-width="2"/><circle cx="13" cy="13" r="3" fill="#555"/></svg></div><h5>Visualize</h5><p>Lorem ipsum is simply dummy text of the printing and typesetting industry. Lorem ipsum has been the standard.</p></div>
    <div class="card"><div class="icon"><svg width="26" height="26" viewBox="0 0 26 26"><circle cx="11" cy="11" r="7" fill="none" stroke="#555" stroke-width="2"/><line x1="16" y1="16" x2="23" y2="23" stroke="#555" stroke-width="2"/></svg></div><h5>Discover</h5><p>Lorem ipsum is simply dummy text of the printing and typesetting industry. Lorem ipsum has been the standard.</p></div>
  </div>
</section>

<section class="news">
  <div class="section-title">
    <div class="kicker">Our Companies Recent Activities</div>
    <h2>COMPANY NEWS</h2>
  </div>
  <div class="news-box">
    <div class="news-img" role="img" aria-label="Pair of reading glasses on a desk"></div>
    <p>Lorem ipsum is simply dummy text of the printing and typesetting industry. Lorem ipsum has been the industry standard dummy text ever since, when an unknown printer took a galley of type and scrambled it to make a type specimen book for the printing trade.</p>
    <div class="news-person">
      <div class="avatar" role="img" aria-label="Portrait of the award recipient"></div>
      <div><b>Lena Marsh, Director of Harbor Capital Group</b>Regional Award</div>
    </div>
  </div>
  <div class="dots"><i></i><i class="on"></i><i></i></div>
</section>

<footer class="site-footer">
  <div class="foot-grid">
    <div class="foot-col">
      <div class="foot-brand"><i></i>OVIN PR</div>
      <p>Lorem ipsum is simply dummy text of the printing and typesetting industry today.</p>
      <div class="socials"><i></i><i></i><i></i><i></i><i></i></div>
    </div>
    <div class="foot-col">
      <h6>Contact</h6>
      <p>Qianhai District, Shenzhen</p>
      <p>+86 755 0100 2200</p>
      <p>hello@ovinpr.example</p>
    </div>
    <div class="foot-col">
      <h6>Resources</h6>
      <ul><li>Downloads</li><li>Testimonial</li><li>Features</li><li>Blog</li></ul>
    </div>
    <div class="foot-col" style="width:240px">
      <h6>Subscribe</h6>
      <p>Subscribe to our newsletter to receive news and updates from our team.</p>
      <div class="sub-input"></div>
      <div class="sub-btn">Subscribe</div>
    </div>
  </div>
</footer>
<div class="foot-bottom">
  <div class="wrap">
    <span>© OVIN PR, Inc. All rights reserved.</span>
    <div class="links"><span>Services</span><span>How it Works</span><span>Employer</span><span>Resources</span><span>Blog</span></div>
  </div>
</div>

</body>
</html>
```